Upscale business cards needed for family office

We would like professional business cards created for employees of our family office. Relatively simple and straightforward, but also with a unique element to set them apart. Probably stick with neutral and simple colors that mesh well with the colors in the logo. We need space for the traditional elements, including name, title, address, email/phone number.

Industry/Entity Type

Business

Contact Information for Business Card

Space for name, title, phone number, email, address

```html
<!DOCTYPE html>
<html lang="en">
<head>
<meta charset="UTF-8">
<title>H&amp;R Business Cards</title>
<link href="https://fonts.googleapis.com/css2?family=Source+Sans+3:wght@400;600&display=swap" rel="stylesheet">
<style>
  :root {
    --page-bg: #eceae7;
    --card-white: #ffffff;
    --blue-top: #0896c6;
    --blue-bottom: #3a70b6;
    --card-black: #231f20;
    --mark-grey: #5a5a5a;
    --mark-light: #8d8d8d;
    --text-light: #ffffff;
  }
  html, body {
    margin: 0;
    padding: 0;
    width: 1200px;
    height: 900px;
    overflow: hidden;
    background: var(--page-bg);
    font-family: "Source Sans 3", "Myriad Pro", sans-serif;
  }
  .canvas {
    position: relative;
    width: 1200px;
    height: 900px;
  }
  .card {
    position: absolute;
    box-shadow: 0 4px 14px rgba(0,0,0,0.18);
    overflow: hidden;
  }
  .card-front {
    left: 238px;
    top: 61px;
    width: 555px;
    height: 343px;
    background: var(--card-white);
  }
  .front-panel {
    position: absolute;
    left: 0;
    top: 0;
    width: 295px;
    height: 343px;
    background: linear-gradient(180deg, var(--blue-top), var(--blue-bottom));
  }
  .front-notch {
    position: absolute;
    left: 264px;
    top: 47px;
    width: 40px;
    height: 249px;
    background: var(--card-white);
  }
  .contact {
    position: absolute;
    left: 34px;
    top: 80px;
    color: var(--text-light);
  }
  .contact-name {
    font-size: 23px;
    font-weight: 400;
    line-height: 1.1;
    margin: 0;
  }
  .contact-title {
    font-size: 15px;
    margin: 2px 0 0;
  }
  .contact-address {
    font-size: 15px;
    line-height: 19px;
    margin: 16px 0 0;
  }
  .contact-lines {
    list-style: none;
    padding: 0;
    margin: 15px 0 0;
    font-size: 15px;
    line-height: 20px;
  }
  .contact-lines li {
    display: flex;
    align-items: center;
    gap: 8px;
  }
  .contact-lines svg {
    width: 12px;
    height: 12px;
    flex: none;
  }
  .brand-name {
    position: absolute;
    font-weight: 400;
    letter-spacing: 1px;
    margin: 0;
    text-align: center;
  }
  .card-front .brand-name {
    left: 290px;
    top: 0;
    width: 178px;
    height: 343px;
    line-height: 343px;
    font-size: 56px;
    color: var(--mark-grey);
  }
  .card-back {
    left: 457px;
    top: 518px;
    width: 560px;
    height: 343px;
    background: var(--card-black);
  }
  .card-back .brand-name {
    left: 0;
    top: 0;
    width: 560px;
    height: 343px;
    line-height: 343px;
    font-size: 60px;
    color: var(--mark-light);
  }
</style>
</head>
<body>
<main class="canvas">
  <section class="card card-front" aria-label="Business card front">
    <div class="front-panel"></div>
    <div class="front-notch"></div>
    <div class="contact">
      <h1 class="contact-name">Daniel Hart</h1>
      <p class="contact-title">Managing Director</p>
      <p class="contact-address">12345, Address Goes Here<br>Country Name, 123456.</p>
      <ul class="contact-lines">
        <li>
          <svg viewBox="0 0 12 12" aria-hidden="true"><path fill="#fff" d="M2.5 1l2 2.2-1 1.3c.7 1.4 1.6 2.3 3 3l1.3-1 2.2 2-1.2 1.5C5.6 10 2 6.4 1 2.2z"/></svg>
          044-987 654 321
        </li>
        <li>
          <svg viewBox="0 0 12 12" aria-hidden="true"><rect x="1" y="2.5" width="10" height="7" fill="#fff"/><path d="M1 2.8l5 3.8 5-3.8" fill="none" stroke="#2f7dbd" stroke-width="1"/></svg>
          hello@mailname.com
        </li>
        <li>
          <svg viewBox="0 0 12 12" aria-hidden="true"><g fill="none" stroke="#fff" stroke-width="1.4" stroke-linecap="round"><path d="M5 7l2-2"/><path d="M6.3 3.2l1-1a2 2 0 012.8 2.8l-1 1"/><path d="M5.7 8.8l-1 1a2 2 0 01-2.8-2.8l1-1"/></g></svg>
          www.sitename.com
        </li>
      </ul>
    </div>
    <p class="brand-name">H&amp;R</p>
  </section>

  <section class="card card-back" aria-label="Business card back">
    <p class="brand-name">H&amp;R</p>
  </section>
</main>
</body>
</html>
```